依頼詳細
山形本社にて弊社最大規模の展示会を7月に行います。販売店様用のチラシの作成をお願い致します。商品構成については、ファッション・バッグ・靴・健康ジュエリーなど多数に及びますので、商品コーナー毎の記載をお願い致します。チラシのサイズはA2で4つ折り表裏でお願い致します。
記載項目
社名に関しては、各販売店用として使って頂くので、チラシの裏右下に空欄を設けてもらえると助かります。/展示会名:「ソレイユフェア(仮)」、日時:7/18(金)~7/22(火)9:30~18:00(22日のみ9:30~17:00)、会場:カルデン本社展示場、TEL:023-481-7926、住所:〒990-4127 山形県山形市若葉台5-3-11/各商品写真(添付)、各商品に対しての簡易コメント
サイズ
A2(縦594×横420mm)
ページ数
両面
希望イメージ
シンプル 複雑
単色 カラフル
暗い 明るい
日常 高級
遊び心 厳粛
未来的 伝統的
女性的 男性的
希望する色
赤 黄 緑
納品ファイル
• 高解像度JPG (.jpg)
• イラストレーター形式 (.ai)
補足説明
商品画像については、随時添付させていただきますので、
まずは表紙のデザインだけでもいいので上げていただければ幸いです。
また、「ソレイユフェア」がタイトルなのですが、サブタイトルが未定でございます。
もしよろしければ、サブタイトルも一緒に上げていただければ幸いです。
過去のソレイユフェアの表紙と、去年のソレイユフェアのチラシ構成を添付させていただきますので、
参考にして頂ければ幸いです。何卒宜しくお願い致します。
現在まででチラシに記載する商品画像を添付いたします。

表紙のみでも作成頂ければと思いますので、何卒宜しくお願い致します。

いつものチラシとは違ったデザインであったため、新鮮であったのと、サブタイトルも良かったです。

大変面倒な依頼でしたが、ご提案頂き、ありがとうございました。

```html
<!DOCTYPE html>
<html lang="ja">
<head>
<meta charset="utf-8">
<title>ソレイユフェア 2014</title>
<link rel="stylesheet" href="https://fonts.googleapis.com/css2?family=M+PLUS+Rounded+1c:wght@800;900&family=Zen+Maru+Gothic:wght@700;900&family=Noto+Serif+JP:wght@600;700;900&family=Cinzel:wght@700&family=Noto+Sans+JP:wght@500;700&display=swap">
<style>
  :root {
    --rose-deep: #e0457f;
    --rose: #f08cb0;
    --rose-pale: #fbd9e6;
    --cream: #fff8f6;
    --gold: #e8b93a;
    --gold-light: #fff0a8;
    --gold-dark: #8f5a12;
    --title-red: #b0123a;
    --ink: #3a1a22;
    --ribbon: #e36fa2;
    --ribbon-dark: #b8427a;
  }
  * { margin: 0; padding: 0; box-sizing: border-box; }
  html, body { width: 848px; height: 1200px; overflow: hidden; background: #fff; }
  .flyer-cover {
    position: relative;
    width: 848px;
    height: 1200px;
    overflow: hidden;
    font-family: "Noto Sans JP", sans-serif;
    color: var(--ink);
  }
  .rose-backdrop {
    position: absolute; inset: 0;
    background:
      radial-gradient(ellipse 330px 430px at 50% 52%, var(--cream) 0%, rgba(255,248,246,0.92) 55%, rgba(255,248,246,0) 100%),
      radial-gradient(circle at 12% 12%, #f6a3c0 0%, rgba(246,163,192,0) 28%),
      radial-gradient(circle at 88% 90%, #f27aa3 0%, rgba(242,122,163,0) 30%),
      radial-gradient(circle at 10% 88%, #f59fb8 0%, rgba(245,159,184,0) 30%),
      radial-gradient(circle at 90% 14%, #f8b6cb 0%, rgba(248,182,203,0) 30%),
      linear-gradient(160deg, var(--rose-pale), var(--rose));
  }
  .laurel-wreath {
    position: absolute;
    left: 250px; top: 150px;
    width: 360px; height: 400px;
    border-radius: 50% 50% 45% 45%;
    background: radial-gradient(ellipse at 50% 50%, rgba(255,255,255,0) 52%, rgba(232,185,58,0.55) 58%, rgba(200,150,40,0.65) 68%, rgba(232,185,58,0) 74%);
  }
  .tagline {
    position: absolute;
    writing-mode: vertical-rl;
    font-family: "Zen Maru Gothic", sans-serif;
    font-weight: 900;
    color: var(--rose-deep);
    -webkit-text-stroke: 8px #fff;
    paint-order: stroke fill;
    letter-spacing: 0.04em;
  }
  .tagline--right { right: 40px; top: 18px; font-size: 44px; }
  .tagline--left { left: 26px; top: 112px; font-size: 42px; }
  .event-title {
    position: absolute;
    left: 0; right: 0; top: 258px;
    text-align: center;
    font-family: "M PLUS Rounded 1c", sans-serif;
    font-weight: 900;
    line-height: 1.0;
    color: var(--gold);
    -webkit-text-stroke: 10px var(--title-red);
    paint-order: stroke fill;
  }
  .event-title__line { display: block; font-size: 104px; }
  .event-title__line--first { margin-left: -20px; letter-spacing: -0.04em; }
  .event-title__line--second { margin-left: 90px; margin-top: 6px; }
  .event-title-latin {
    position: absolute; left: 0; right: 0; top: 505px;
    text-align: center;
    font-family: "Cinzel", serif;
    font-weight: 700;
    font-size: 50px;
    color: var(--gold);
    -webkit-text-stroke: 5px var(--gold-dark);
    paint-order: stroke fill;
    letter-spacing: 0.02em;
  }
  .host-ribbon {
    position: absolute; left: 252px; top: 580px;
    width: 344px; height: 86px;
  }
  .host-ribbon__name {
    position: absolute; left: 0; right: 0; top: 16px;
    text-align: center;
    font-family: "Zen Maru Gothic", sans-serif;
    font-weight: 700;
    font-size: 30px;
    color: #fff;
    letter-spacing: 0.1em;
  }
  .event-schedule {
    position: absolute; left: 270px; top: 674px;
    font-family: "Noto Serif JP", serif;
    color: var(--ink);
  }
  .event-schedule__year { font-size: 30px; font-weight: 700; }
  .event-schedule__dates { font-size: 76px; font-weight: 900; line-height: 1.05; letter-spacing: -0.02em; }
  .event-schedule__dates small { font-size: 48px; }
  .day-mark {
    display: inline-block; width: 34px; height: 34px; border-radius: 50%;
    background: var(--ink); color: #fff;
    font-size: 22px; line-height: 34px; text-align: center;
    vertical-align: 14px; margin: 0 2px;
  }
  .event-schedule__hours { font-family: "Noto Sans JP", sans-serif; font-size: 20px; font-weight: 500; margin-top: 4px; }
  .venue-info { position: absolute; left: 262px; top: 826px; }
  .venue-info__name { font-size: 34px; font-weight: 700; }
  .venue-info__tel { font-size: 20px; font-weight: 500; margin-left: 118px; margin-top: 4px; }
  .venue-info__address { font-size: 18px; font-weight: 500; margin-left: 118px; }
</style>
</head>
<body>
  <main class="flyer-cover">
    <div class="rose-backdrop" role="img" aria-label="ピンクと赤のバラの花が画面いっぱいに咲く背景"></div>
    <div class="laurel-wreath" role="img" aria-label="金色の月桂冠の飾り"></div>

    <p class="tagline tagline--right">華やかに輝く世代にお届けする</p>
    <p class="tagline tagline--left">美と健康とお買い得の５日間です。</p>

    <h1 class="event-title">
      <span class="event-title__line event-title__line--first">ソレイユ</span>
      <span class="event-title__line event-title__line--second">フェア</span>
    </h1>
    <p class="event-title-latin">SOLEIL FAIR</p>

    <div class="host-ribbon">
      <svg width="344" height="86" viewBox="0 0 344 86" aria-hidden="true">
        <path d="M0 22 L52 22 L40 44 L52 66 L0 66 L16 44 Z" fill="var(--ribbon-dark)"/>
        <path d="M344 22 L292 22 L304 44 L292 66 L344 66 L328 44 Z" fill="var(--ribbon-dark)"/>
        <path d="M36 12 Q172 36 308 12 L308 60 Q172 84 36 60 Z" fill="var(--ribbon)"/>
      </svg>
      <p class="host-ribbon__name">カルデン</p>
    </div>

    <section class="event-schedule">
      <p class="event-schedule__year">2014年</p>
      <p class="event-schedule__dates">7<small>月</small>18<span class="day-mark">金</span>〜22<span class="day-mark">火</span></p>
      <p class="event-schedule__hours">9:30〜18:00（22日のみ9:30〜17:00）</p>
    </section>

    <section class="venue-info">
      <p class="venue-info__name">会場：カルデン本社展示場</p>
      <p class="venue-info__tel">TEL：023-481-7926</p>
      <p class="venue-info__address">〒990-4127 山形県山形市若葉台5-3-11</p>
    </section>
  </main>
</body>
</html>
```